Business card design for upmarket Home Technology design and Installation company

Hello designers, we need a great business card designed.
We need it to convey high tech, and also sophistication .
We work with some of the most affluent people in the world building them home technology systems, and A/V entertainment systems.

Services offered include the following:
Design, sales, installation, and maintenance of

*Home Automation systems
*Distributed / Multi-Room Audio and Video
*High Performance Networks & WiFi
* Lighting and Shade Control
*Home cinema
*Security and CCTV Systems

I have included a copy of our logo to use for your design efforts.

Target Market(s)

Upmarket clients with multi million euro villas.

Industry/Entity Type

Home technology

Contact Information for Business Card

NAME: Derek Halloran ADDRESS: Plaza Brisa Local 42, Port Vellamar, 07392 PHONE: +34-602-518-794 EMAIL: DHalloran@VELTRAsmarthomes.com WEB: www.veltrasmarthomes.com

Requirements
Must have
• Our Logo, and our tagline

```html
<!DOCTYPE html>
<html lang="en">
<head>
<meta charset="utf-8">
<title>Veltra Smarter Homes – Business Card</title>
<link rel="stylesheet" href="https://fonts.googleapis.com/css2?family=Lato:wght@400;700;900&family=Open+Sans:wght@400;600;700&display=swap">
<style>
  :root {
    --backdrop: #2b2f31;
    --ink: #141414;
    --ink-soft: #1c1c1c;
    --gold-light: #f2d99b;
    --gold-mid: #d4b26a;
    --gold-deep: #b8923f;
    --text-light: #e4e4e4;
    --text-dark: #1a1a1a;
  }
  * { margin: 0; padding: 0; box-sizing: border-box; }
  html, body { width: 1200px; height: 1122px; overflow: hidden; }
  body {
    background: var(--backdrop);
    font-family: "Open Sans", sans-serif;
    position: relative;
  }
  .card {
    position: absolute;
    left: 170px;
    width: 860px;
    height: 490px;
    border-radius: 30px;
    overflow: hidden;
  }

  /* ---------- Back: services ---------- */
  .card-back {
    top: 48px;
    background: linear-gradient(100deg, var(--gold-light) 0%, var(--gold-mid) 55%, var(--gold-deep) 100%);
    color: var(--text-dark);
  }
  .brand-block {
    position: absolute;
    left: 70px;
    top: 150px;
    width: 260px;
    text-align: center;
  }
  .brand-dot {
    display: block;
    width: 110px;
    height: 110px;
    margin: 0 auto 26px;
    border-radius: 50%;
    background: var(--text-dark);
  }
  .brand-name {
    font-family: "Lato", sans-serif;
    font-weight: 700;
    font-size: 46px;
    letter-spacing: 6px;
    line-height: 1;
  }
  .brand-tagline {
    font-family: "Lato", sans-serif;
    font-weight: 700;
    font-size: 13px;
    letter-spacing: 7px;
    margin-top: 10px;
  }
  .services {
    position: absolute;
    left: 370px;
    top: 120px;
    width: 460px;
  }
  .services-title {
    font-family: "Lato", sans-serif;
    font-weight: 900;
    font-size: 19px;
    letter-spacing: 0.5px;
    margin-bottom: 8px;
  }
  .services-list { list-style: none; }
  .services-list li {
    font-size: 16.5px;
    line-height: 31px;
    padding-left: 26px;
    position: relative;
  }
  .services-list li::before {
    content: "";
    position: absolute;
    left: 2px;
    top: 11px;
    width: 10px;
    height: 10px;
    border: 2px solid var(--text-dark);
    border-radius: 50%;
  }

  /* ---------- Front: contact ---------- */
  .card-front {
    top: 584px;
    background: var(--ink);
    color: var(--text-light);
  }
  .front-brand {
    position: absolute;
    right: 70px;
    top: 60px;
    display: flex;
    align-items: center;
    gap: 16px;
    color: var(--gold-mid);
  }
  .front-brand .brand-dot {
    width: 44px;
    height: 44px;
    margin: 0;
    background: var(--gold-mid);
  }
  .front-brand .brand-tagline { color: var(--gold-mid); }
  .front-brand .brand-name { font-size: 52px; }
  .person {
    position: absolute;
    left: 70px;
    top: 215px;
  }
  .person-name {
    font-family: "Lato", sans-serif;
    font-weight: 900;
    font-size: 40px;
    letter-spacing: 1px;
    color: var(--gold-mid);
    line-height: 1;
  }
  .person-role {
    font-size: 18px;
    margin-top: 6px;
    color: var(--text-light);
  }
  .divider {
    position: absolute;
    left: 70px;
    right: 70px;
    top: 300px;
    height: 1.5px;
    background: var(--gold-mid);
  }
  .contact {
    position: absolute;
    left: 70px;
    top: 322px;
    list-style: none;
  }
  .contact li {
    display: flex;
    align-items: center;
    gap: 14px;
    font-size: 18px;
    line-height: 36px;
  }
  .contact .phone { font-weight: 700; }
  .contact svg { width: 18px; height: 18px; flex: none; }
  .address {
    position: absolute;
    right: 70px;
    top: 318px;
    text-align: right;
    font-size: 18px;
    line-height: 30px;
    font-style: normal;
  }
  .gold-band {
    position: absolute;
    left: 0;
    bottom: 0;
    width: 860px;
    height: 80px;
  }
  .website {
    position: absolute;
    right: 40px;
    bottom: 16px;
    font-size: 17px;
    color: var(--text-dark);
  }
</style>
</head>
<body>

  <section class="card card-back" aria-label="Card back">
    <div class="brand-block">
      <span class="brand-dot"></span>
      <div class="brand-name">VELTRA</div>
      <div class="brand-tagline">SMARTER HOMES</div>
    </div>
    <div class="services">
      <h2 class="services-title">SERVICES OFFERED INCLUDE THE FOLLOWING:</h2>
      <ul class="services-list">
        <li>Design, sales, installation, &amp; maintenance of</li>
        <li>Home Automation Systems</li>
        <li>Distributed / Multi-Room Audio &amp; Video</li>
        <li>High Performance Networks &amp; WiFi</li>
        <li>Lighting &amp; Shade Control</li>
        <li>Home Cinema</li>
        <li>Security &amp; CCTV Systems</li>
      </ul>
    </div>
  </section>

  <section class="card card-front" aria-label="Card front">
    <div class="front-brand">
      <span class="brand-dot"></span>
      <div>
        <div class="brand-name">VELTRA</div>
        <div class="brand-tagline">SMARTER HOMES</div>
      </div>
    </div>

    <div class="person">
      <div class="person-name">DEREK HALLORAN</div>
      <div class="person-role">Managing Director</div>
    </div>
    <div class="divider"></div>

    <ul class="contact">
      <li class="phone">
        <svg viewBox="0 0 24 24" aria-hidden="true"><path fill="#d4b26a" d="M6.6 10.8a15.1 15.1 0 0 0 6.6 6.6l2.2-2.2c.3-.3.7-.4 1-.2 1.1.4 2.3.6 3.6.6.6 0 1 .4 1 1V20c0 .6-.4 1-1 1A17 17 0 0 1 3 4c0-.6.4-1 1-1h3.5c.6 0 1 .4 1 1 0 1.2.2 2.4.6 3.6.1.3 0 .7-.2 1z"/></svg>
        +34-602-518-794
      </li>
      <li class="email">
        <svg viewBox="0 0 24 24" aria-hidden="true"><rect x="2" y="5" width="20" height="14" rx="1" fill="#d4b26a"/><path d="M2.5 5.5 12 13l9.5-7.5" fill="none" stroke="#141414" stroke-width="1.6"/></svg>
        DHalloran@VELTRAsmarthomes.com
      </li>
    </ul>

    <address class="address">
      Plaza Brisa Local 42<br>
      Port Vellamar 07392
    </address>

    <svg class="gold-band" viewBox="0 0 860 80" preserveAspectRatio="none" aria-hidden="true">
      <defs>
        <linearGradient id="bandGold" x1="0" x2="1" y1="0" y2="0">
          <stop offset="0" stop-color="#f2d99b"/>
          <stop offset="0.6" stop-color="#d4b26a"/>
          <stop offset="1" stop-color="#b8923f"/>
        </linearGradient>
      </defs>
      <path d="M0 62 H520 C548 62 548 22 576 22 H860 V80 H0 Z" fill="url(#bandGold)"/>
    </svg>
    <div class="website">www.veltrasmarthomes.com</div>
  </section>

</body>
</html>
```